Global investment holding company - Business Card Design

Brenvik Holdings is a recently incorporated investment holding company. Based in Singapore, it has operations in global emerging markets in the transport & logistics, energy and livestock industries.

Its tagline "Growth Through Alliance" reflects the company's philosophy of helping countries progress through partnerships which generate employment and share benefits with its society.

We are looking for a business card that reflects our global presence - incorporating the logo design into the business card design. It must have a sophisticated, modern & corporate feel.

Target Market(s)

Investors and high level governmental officials

Industry/Entity Type

Investment

Requirements
Must have
• - Use of shades of blue in logo

-Profile picture

- Name: Dennis Okoro
- Title: Chairman
- Email: dennis@brenvikholdings.example
- Mob: +65 9154 6081
- Tel: +65 6419 5820
- DID: + 65 6419 5821
- Address: 47 Marlow Road, #05-03, Singapore 048812

- website: www.brenvikholdings.example

```html
<!DOCTYPE html>
<html lang="en">
<head>
<meta charset="utf-8">
<title>Brenvik Holdings – Business Card</title>
<link rel="stylesheet" href="https://fonts.googleapis.com/css2?family=Quicksand:wght@400;500;600;700&family=Open+Sans:wght@400;600&display=swap">
<style>
  :root {
    --page-bg: #e9e9e9;
    --blue-dark: #0b4f82;
    --blue-mid: #0a6aa8;
    --blue-light: #1780c2;
    --green-dark: #8fa82a;
    --green-mid: #b5d236;
    --green-light: #d5ec4a;
    --ink-navy: #1d3f63;
    --white: #ffffff;
    --soft-white: #e8eef3;
  }
  * { margin: 0; padding: 0; box-sizing: border-box; }
  html, body {
    width: 1200px; height: 837px; overflow: hidden;
    background: var(--page-bg);
  }
  .card {
    position: absolute; left: 180px; top: 178px;
    width: 840px; height: 480px;
    background: var(--green-mid);
    overflow: hidden;
    font-family: "Quicksand", sans-serif;
  }
  .card__band {
    position: absolute; left: 0; top: 0;
    width: 840px; height: 225px;
    background: radial-gradient(ellipse 70% 90% at 60% 30%, var(--blue-light), var(--blue-mid) 50%, var(--blue-dark));
    border-bottom-right-radius: 22px;
  }
  .card__band::after {
    content: ""; position: absolute; left: 0; top: 225px;
    width: 30px; height: 30px;
    background: var(--blue-dark);
  }
  .card__panel {
    position: absolute; left: 0; top: 225px;
    width: 840px; height: 255px;
    background: radial-gradient(ellipse 60% 90% at 55% 10%, var(--green-light), var(--green-mid) 55%, var(--green-dark));
    border-top-left-radius: 22px;
  }
  .brand {
    position: absolute; left: 48px; top: 78px;
    display: flex; align-items: center; gap: 18px;
  }
  .brand__mark {
    width: 78px; height: 78px; border-radius: 50%;
    background: var(--soft-white);
  }
  .brand__name {
    font-weight: 700; font-size: 38px; line-height: 0.95;
    color: var(--white); letter-spacing: 0.5px;
  }
  .brand__tagline {
    position: absolute; left: 58px; top: 172px;
    font-family: "Open Sans", sans-serif;
    font-size: 15px; letter-spacing: 1.6px;
    color: var(--soft-white);
  }
  .person {
    position: absolute; right: 58px; top: 48px;
    text-align: right; color: var(--white);
  }
  .person__name { font-size: 60px; font-weight: 400; line-height: 1.1; }
  .person__title { font-size: 34px; font-weight: 400; margin-top: 10px; color: var(--soft-white); }
  .photo {
    position: absolute; left: 48px; top: 37px;
    width: 166px; height: 194px; border-radius: 10px;
    background: linear-gradient(160deg, #c9b9a0 0%, #8a7a66 45%, #1f2a3a 100%);
    box-shadow: 0 0 0 6px rgba(255,255,255,0.18);
  }
  .contact {
    position: absolute; left: 248px; top: 34px;
    list-style: none; color: var(--ink-navy);
    font-size: 18px; font-weight: 500; line-height: 30px;
  }
  .contact__label { display: inline-block; min-width: 62px; }
  .website {
    position: absolute; right: 38px; bottom: 20px;
    font-size: 18px; letter-spacing: 3px;
    color: var(--soft-white);
  }
</style>
</head>
<body>
  <article class="card">
    <header class="card__band">
      <div class="brand">
        <span class="brand__mark"></span>
        <span class="brand__name">BRENVIK<br>HOLDINGS</span>
      </div>
      <p class="brand__tagline">GROWTH THROUGH ALLIANCE</p>
      <div class="person">
        <h1 class="person__name">Dennis Okoro</h1>
        <p class="person__title">Chairman</p>
      </div>
    </header>
    <section class="card__panel">
      <div class="photo" role="img" aria-label="Profile photo of Dennis Okoro"></div>
      <ul class="contact">
        <li><span class="contact__label">Email:</span>dennis@brenvikholdings.example</li>
        <li><span class="contact__label">Mob:</span>+65 9154 6081</li>
        <li><span class="contact__label">Tel:</span>+65 6419 5820</li>
        <li><span class="contact__label">DID:</span>+ 65 6419 5821</li>
        <li>Address: 47 Marlow Road, #05-03, Singapore 048812</li>
      </ul>
      <p class="website">www.brenvikholdings.example</p>
    </section>
  </article>
</body>
</html>
```